Single Page/Scrolling Design for Model Recruitment site

We need a design (and if you are capable, coding) for our company, Brimwell Parlour (LA as in Los Angeles). We like modern single page designs, hence the title for the project. We have already had a designer come up with a logo, which is attached. You're free to play around with the colors, although we want the site to have a feminine appeal to it.

The site is basically a recruitment project for girls who are interested in working as chat hosts for cam sites. We don't want anything cheesy that feels like a porn site. The inspiration for the logo (and the inspiration for the site) comes from the French and English salons of the late 18th century, where beautiful and intelligent women would gather to discuss a range of topics. We want the website to convey that this work is fun and exciting. Please keep these things in mind for the design.

As I mentioned, we like the modern look and feel of single page designs, especially because we don't have a ton of content. We just need an "About us" area, a "Work from Home" area, a "Work at The Brimwell Parlour" area, and "Contact Us" area which should have text boxes for entering email, subject, a message, etc.

The logo I mentioned is attached, as well as a very crude mockup of the layout of all the content I described.

Target Market(s)

Women age 18-35.

Industry/Entity Type

It Company

Font styles to use
Serif
Decorative
Script

Colors

Designer to choose colors to be used in the design.

Requirements
Should not have
• Images that are super sexual or even slightly pornographic. We want this to appeal to a broad range of women.

```html
<!DOCTYPE html>
<html lang="en">
<head>
<meta charset="utf-8">
<title>Brimwell Parlour — Webcam Modeling</title>
<link rel="stylesheet" href="https://fonts.googleapis.com/css2?family=Raleway:wght@300;400;500;600;800&display=swap">
<style>
:root{
  --pink:#e0218a;
  --ink:#3a3a3a;
  --muted:#8a8a8a;
  --nav:#262626;
  --paper:#ffffff;
  --sand:#f5f3f0;
  --night:#2b2b2b;
  --footer:#333333;
  --tile-a:#3b5998;
  --tile-b:#55acee;
  --tile-c:#e4268f;
}
*{box-sizing:border-box;margin:0;padding:0}
html,body{width:1200px;height:3194px;overflow:hidden}
body{font-family:'Raleway',sans-serif;color:var(--ink);background:var(--paper);position:relative}
.abs{position:absolute}
.center{left:0;width:1200px;text-align:center}

/* nav */
.site-nav{top:0;left:0;width:1200px;height:80px;background:var(--nav)}
.brand{left:82px;top:22px;display:flex;align-items:center;gap:12px;color:var(--pink);font-size:17px;font-weight:600;letter-spacing:1px}
.brand-dot{width:30px;height:30px;border-radius:50%;background:var(--pink)}
.nav-links{right:100px;top:30px;display:flex;gap:32px;font-size:13px;letter-spacing:2px;text-transform:uppercase;color:#bdbdbd}
.nav-links .active{color:var(--pink)}

/* hero */
.hero{top:80px;left:0;width:1200px;height:509px;background:linear-gradient(135deg,#6e5a5c 0%,#b9a8a6 35%,#8c7675 60%,#4a3f45 100%)}
.hero-title{top:250px;font-size:88px;font-weight:300;color:#fff;letter-spacing:2px;line-height:1}
.hero-title b{font-weight:800}
.hero-rule{top:367px;height:2px;background:rgba(255,255,255,.7);width:170px}
.hero-sub{top:358px;font-size:20px;font-weight:800;color:var(--pink);letter-spacing:.5px}
.hero-btn{left:524px;top:415px;width:155px;height:48px;border:2px solid #fff;color:#fff;font-size:16px;display:flex;align-items:center;justify-content:center;background:rgba(0,0,0,.15)}
.round-arrow{width:74px;height:74px;border:2px solid rgba(255,255,255,.85);border-radius:50%;top:290px}
.scroll-cue{left:575px;top:489px;width:52px;height:52px;border-radius:50%;background:#3a3a3a}

/* section heads */
.sec-title{font-size:40px;font-weight:300;letter-spacing:1px}
.diamonds{display:flex;justify-content:center;gap:10px}
.diamonds span{width:9px;height:9px;border:1.5px solid var(--pink);transform:rotate(45deg)}
.sec-lead{font-size:16px;line-height:1.5;color:var(--muted);width:640px;left:280px;text-align:center}

/* about */
.about-copy{left:100px;top:892px;width:480px;font-size:15px;line-height:2.1;color:var(--muted)}
.about-copy p{margin-bottom:24px}
.about-copy em{font-style:normal;color:var(--pink)}
.outline-btn{left:100px;top:1157px;width:205px;height:56px;border:2px solid #444;font-size:16px;display:flex;align-items:center;justify-content:center;color:#333}
.about-photo{left:663px;top:884px;width:465px;height:338px;background:linear-gradient(120deg,#f1e8cf 0%,#c9ab8a 40%,#7c5a5c 75%,#3a2c34 100%)}

/* train */
.train{top:1335px;left:0;width:1200px;height:450px;background:var(--sand)}
.train-col{top:1592px;width:487px;font-size:16px;line-height:1.55;color:#333}

/* work from home */
.work{top:1785px;left:0;width:1200px;height:454px;background:linear-gradient(160deg,#2c1a10 0%,#8a5228 35%,#c98a4e 55%,#5e3418 80%,#1c100a 100%)}
.work-title{top:1862px;font-size:40px;font-weight:300;color:#fff}
.work-text{top:1946px;left:290px;width:620px;text-align:center;color:#fff;font-size:16px;line-height:1.5;font-weight:500}
.ghost-btn{top:2084px;height:50px;border:2px solid rgba(255,255,255,.8);color:#fff;font-size:16px;display:flex;align-items:center;justify-content:center;letter-spacing:.5px}

/* contact */
.contact{top:2239px;left:0;width:1200px;height:753px;background:var(--night)}
.contact .sec-title{color:#fff}
.contact .sec-lead{color:#bbb}
.field{left:98px;width:474px;border:1.5px solid #666;color:#888;font-size:15px;padding:18px 16px}
.send-btn{left:100px;top:2887px;width:157px;height:48px;background:var(--pink);color:#fff;font-weight:600;font-size:15px;display:flex;align-items:center;justify-content:center}
.contact-info{left:628px;top:2482px;width:470px;color:#777;font-size:16px;line-height:1.45}
.contact-info .addr{margin-top:38px;font-size:20px;color:#999;line-height:1.5}
.contact-info .phones{margin-top:24px;font-size:20px;color:#999;line-height:1.5}
.drop-line{margin-top:34px;display:flex;align-items:center;gap:14px;color:var(--pink);font-size:15px}

/* footer */
.footer{top:2992px;left:0;width:1200px;height:202px;background:var(--footer)}
.tile{top:2992px;width:328px;height:202px;color:#fff}
.tile-name{position:absolute;left:18px;top:20px;font-size:18px}
.tile-mark{position:absolute;left:144px;top:86px;width:40px;height:40px;border-radius:50%;border:3px solid #fff}
</style>
</head>
<body>

<header class="abs site-nav">
  <div class="abs brand"><span class="brand-dot"></span>Brimwell Parlour</div>
  <nav class="abs nav-links">
    <span class="active">Home</span><span>About</span><span>Train @ The Parlour</span><span>Work from Home</span><span>Contact</span>
  </nav>
</header>

<section class="abs hero" role="img" aria-label="Photo of a woman's legs in white knitted socks on a wooden floor"></section>
<div class="abs round-arrow" style="left:15px">
  <svg width="70" height="70" viewBox="0 0 70 70"><path d="M40 25 L30 35 L40 45" stroke="#fff" stroke-width="2.5" fill="none"/></svg>
</div>
<div class="abs round-arrow" style="left:1111px">
  <svg width="70" height="70" viewBox="0 0 70 70"><path d="M30 25 L40 35 L30 45" stroke="#fff" stroke-width="2.5" fill="none"/></svg>
</div>
<h1 class="abs center hero-title">WEBCAM <b>MODELING</b></h1>
<div class="abs hero-rule" style="left:225px"></div>
<div class="abs hero-rule" style="left:805px"></div>
<p class="abs center hero-sub">WELCOME TO THE BRIMWELL PARLOUR</p>
<div class="abs hero-btn">START NOW!</div>
<div class="abs scroll-cue">
  <svg width="52" height="52" viewBox="0 0 52 52"><path d="M19 22 L26 29 L33 22" stroke="#fff" stroke-width="3" fill="none"/></svg>
</div>

<!-- about -->
<h2 class="abs center sec-title" style="top:666px">ABOUT US</h2>
<div class="abs center diamonds" style="top:727px"><span></span><span></span><span></span><span></span></div>
<p class="abs sec-lead" style="top:752px">The Brimwell Parlour was started with the understanding that there is a large number of women sho are curious about working in webcam entertainment but have no idea where to start.</p>
<div class="abs about-copy">
  <p>There are hundreds of <em>'studios'</em> or <em>'agencies'</em> on the internet with the goal of making money just by getting you to sign up, or even worse, by <em>taking a percentage of your comissions</em> once you do.</p>
  <p>That is not what <em>The Brimwell Parlour</em> is about. We want to be the premier destination for webcam entertainers to further their careers, <em>no matter</em> what level of experiece you have.</p>
</div>
<div class="abs outline-btn">START NOW!</div>
<div class="abs about-photo" role="img" aria-label="Soft sunlit photo of a blonde woman in profile"></div>

<!-- train -->
<section class="abs train"></section>
<h2 class="abs center sec-title" style="top:1401px">TRAIN @ BRIMWELL PARLOUR</h2>
<div class="abs center diamonds" style="top:1462px"><span></span><span></span><span></span><span></span></div>
<p class="abs sec-lead" style="top:1487px">Neque porro quisquam est, qui dolorem ipsum quia dolor sit amet consectetur, adipisci velit, sed quia non numquam</p>
<p class="abs train-col" style="left:98px">There are hundreds of 'studios' or 'agencies' on the internet with the goal of making money just by getting you to sign up, or even worse, by taking a percentage of your comissions once you do. That is not what The Brimwell Parlour is about.</p>
<p class="abs train-col" style="left:615px">There are hundreds of 'studios' or 'agencies' on the internet with the goal of making money just by getting you to sign up, or even worse, by taking a percentage of your comissions once you do. That is not what The Brimwell Parlour is about.</p>

<!-- work from home -->
<section class="abs work" role="img" aria-label="Warm close-up photo of a reclining body with polka-dot fabric"></section>
<h2 class="abs center work-title">WORK FROM HOME</h2>
<p class="abs work-text">Working as a webcam entertainer can be a very lucrative business, whether it is your only job or something you do on the side. It gives you the flexibility to create your own schedule based around your availability.</p>
<div class="abs ghost-btn" style="left:327px;width:201px">WHAT DO I NEED?</div>
<div class="abs ghost-btn" style="left:665px;width:214px">HOW DO I SIGN UP?</div>

<!-- contact -->
<section class="abs contact"></section>
<h2 class="abs center sec-title" style="top:2293px;color:#fff">CONTACT US</h2>
<div class="abs center diamonds" style="top:2355px"><span></span><span></span><span></span><span></span></div>
<p class="abs sec-lead" style="top:2382px;color:#bbb">Neque porro quisquam est, qui dolorem ipsum quia dolor sit amet consectetur, adipisci velit, sed quia non numquam</p>
<div class="abs field" style="top:2485px;height:55px;padding-top:16px">Your Name</div>
<div class="abs field" style="top:2566px;height:53px;padding-top:16px">Your Email</div>
<div class="abs field" style="top:2645px;height:213px">Your Message</div>
<div class="abs send-btn">SEND</div>
<div class="abs contact-info">
  <p>Lorem ipsum dolor sit amet, consectetuer adipiscing elit. Donec odio. Quisque volutpat mattis eros. Nullam malesuada erat ut turpis. Suspendisse urna nibh, viverra non, semper suscipit, posuere a, pede.</p>
  <p class="addr">4410 Marlow Crest Avenue<br>Los Angeles, California</p>
  <p class="phones">T: (555) 014-2290<br>M: (555) 018-7731</p>
  <div class="drop-line">
    <svg width="44" height="44" viewBox="0 0 44 44"><rect x="8" y="8" width="28" height="28" transform="rotate(45 22 22)" fill="#444"/><rect x="14" y="16" width="16" height="12" fill="none" stroke="#888" stroke-width="1.5"/><path d="M14 16 L22 23 L30 16" fill="none" stroke="#888" stroke-width="1.5"/></svg>
    Drop us a line!
  </div>
</div>

<!-- footer -->
<footer class="abs footer"></footer>
<div class="abs tile" style="left:111px;background:var(--tile-a)"><span class="tile-name">Circlepage</span><span class="tile-mark"></span></div>
<div class="abs tile" style="left:439px;background:var(--tile-b)"><span class="tile-name">Chirpline</span><span class="tile-mark"></span></div>
<div class="abs tile" style="left:766px;background:var(--tile-c)"><span class="tile-name">Plusring</span><span class="tile-mark"></span></div>

</body>
</html>
```